An e-flyer for an exotic car and fine wine club.

This is the first meeting of Birchwell Motor Society and includes several businesses. Their logos should be featured at the bottom. It should be sleek, elegant and simple featuring a photo of an Corvane Lestrel R7 as well as my logo (I will provide photos). The flyer needs to look professional and appeal to billionaires.
The text should read:
Birchwell Motor society presents
Fast Cars and Fine Wine (but not while driving)
Hosted by Harlow Gem Vault
Bring your best car(s) and join us to enjoy the party with sommelier selected wines, the best classic and modern cars and hors d'oeuvre catered by Penrose's Clam House. Live DJ.
August 26th 3-6 p.m.
This event is gratis.
RSVP to dana@birchwellmotors.example for address and details

Target Market(s)
Very wealthy exotic car owners
Industry/Entity Type
Car Club, Fine Wines.
Requirements
Must have
- Style, panache, elegance, sleekness, simplicity. I like the idea of a black or dark flyer with a consistent color scheme.
Nice to have
- I want the flyer to be simple and sleek, feature an Corvane Lestrel R7 as the eye catcher, Birchwell Motor Society logo featured prominently on the top, and the other business logos on the bottom.
Should not have
- It must not be too noisy or busy.

```html
<!DOCTYPE html>
<html lang="en">
<head>
<meta charset="utf-8">
<title>Fast Cars and Fine Wine — Birchwell Motor Society</title>
<link href="https://fonts.googleapis.com/css2?family=Oswald:wght@500&family=Poppins:ital,wght@0,400;0,600;1,400&display=swap" rel="stylesheet">
<style>
  :root {
    --stage: #a4a4a4;
    --ink: #0c0c0c;
    --white: #f4f4f4;
    --silver: #cfcfcf;
    --grey: #a9a9a9;
    --brand: #e96a1c;
    --rule: #8d8d8d;
  }
  * { margin: 0; padding: 0; box-sizing: border-box; }
  html, body { width: 1200px; height: 1200px; overflow: hidden; background: var(--stage); }
  .flyer {
    position: absolute; left: 209px; top: 30px; width: 782px; height: 1107px;
    overflow: hidden; color: var(--white);
    font-family: "Poppins", sans-serif;
    background: linear-gradient(180deg, #8b8b8b 0%, #6c6c6c 22%, #3e3e3e 45%, #161616 60%, var(--ink) 100%);
  }
  .abs { position: absolute; }
  .brand { left: 0; width: 100%; top: 48px; text-align: center; color: var(--brand); font-weight: 600; }
  .brand-name { font-size: 64px; line-height: 1; letter-spacing: 4px; text-transform: uppercase; }
  .brand-sub { font-size: 30px; letter-spacing: 18px; margin-top: 14px; text-transform: uppercase; padding-left: 18px; }
  .presents { left: 0; width: 100%; top: 237px; text-align: center; font-style: italic; font-size: 21px; letter-spacing: 13px; text-transform: uppercase; }
  .hero-car {
    left: 33px; top: 296px; width: 727px; height: 296px; border-radius: 46% 40% 18% 18% / 60% 55% 20% 20%;
    background: radial-gradient(ellipse at 55% 45%, #b8242a 0%, #8e151b 55%, #3a0b0d 100%);
  }
  .headline { left: 0; width: 100%; top: 628px; text-align: center; font-family: "Oswald", sans-serif; font-weight: 500; font-size: 64px; line-height: 1; color: var(--silver); letter-spacing: -1px; text-transform: uppercase; }
  .headline-rule { left: 55px; width: 672px; top: 695px; height: 2px; background: linear-gradient(90deg, transparent, #e0e0e0 20%, #e0e0e0 80%, transparent); }
  .aside { right: 78px; top: 702px; font-style: italic; font-size: 18px; letter-spacing: 1px; }
  .host { left: 0; width: 100%; top: 738px; text-align: center; font-size: 28px; text-transform: uppercase; }
  .corner { width: 38px; height: 35px; border: 0 solid var(--white); }
  .c-tl { left: 55px; top: 793px; border-top-width: 2px; border-left-width: 2px; }
  .c-tr { left: 689px; top: 793px; border-top-width: 2px; border-right-width: 2px; }
  .c-bl { left: 55px; top: 914px; border-bottom-width: 2px; border-left-width: 2px; }
  .c-br { left: 689px; top: 914px; border-bottom-width: 2px; border-right-width: 2px; }
  .invite { left: 0; width: 100%; top: 807px; text-align: center; text-transform: uppercase; }
  .invite-lead { font-style: italic; font-size: 14px; line-height: 17px; }
  .invite-detail { font-weight: 600; font-size: 14.6px; line-height: 18px; letter-spacing: .6px; margin-top: 3px; }
  .invite-rule { left: 170px; width: 442px; top: 890px; height: 2px; background: linear-gradient(90deg, transparent, var(--rule) 15%, var(--rule) 85%, transparent); }
  .when { left: 0; width: 100%; top: 897px; text-align: center; font-family: "Oswald", sans-serif; font-weight: 500; font-size: 35px; line-height: 1.1; text-transform: uppercase; letter-spacing: -.3px; }
  .when-free { color: var(--grey); }
  .rsvp { left: 0; width: 100%; top: 973px; text-align: center; font-size: 15px; text-transform: uppercase; letter-spacing: .4px; }
  .rsvp b { font-weight: 600; }
  .partners { left: 0; width: 100%; top: 1042px; display: flex; justify-content: center; gap: 46px; }
  .partner { font-weight: 600; font-size: 17px; letter-spacing: 1px; color: var(--white); text-transform: uppercase; }
</style>
</head>
<body>
  <main class="flyer" role="img" aria-label="Overcast sky over a racetrack fading into a dark wet floor">
    <header class="abs brand">
      <div class="brand-name">Birchwell</div>
      <div class="brand-sub">Motor Society</div>
    </header>
    <p class="abs presents">Presents</p>

    <div class="abs hero-car" role="img" aria-label="Photo of a red Corvane Lestrel R7 classic coupe on a track, reflected on the wet ground"></div>

    <h1 class="abs headline">Fast Cars and Fine Wine</h1>
    <div class="abs headline-rule"></div>
    <p class="abs aside">(BUT NOT WHILE DRIVING)</p>
    <p class="abs host">| Hosted by Harlow Gem Vault |</p>

    <span class="abs corner c-tl"></span>
    <span class="abs corner c-tr"></span>
    <span class="abs corner c-bl"></span>
    <span class="abs corner c-br"></span>

    <section class="abs invite">
      <p class="invite-lead">Bring your best car(s) and join us to<br>enjoy the party with</p>
      <p class="invite-detail">Sommelier selected wines, the best classic and<br>modern cars and hors d'oeuvre catered by Penrose's Clam House. Live DJ.</p>
    </section>
    <div class="abs invite-rule"></div>
    <p class="abs when">August 26th 3-6 p.m. | <span class="when-free">This event is gratis.</span></p>

    <p class="abs rsvp">RSVP to <b>dana@birchwellmotors.example</b> for address and details</p>

    <footer class="abs partners">
      <span class="partner">Ellery Wine House</span>
      <span class="partner">Harlow Gem Vault</span>
    </footer>
  </main>
</body>
</html>
```